Copper Gavel Auctions business card design with existing logo

Looking for a sleek and sexy design using our current logo

Contact Information for Business Card

Name, address, email, phone, website. Marcus Delvane 418 Birchmont Road Suite 200C Fenwick NY 11093 Copperbidhouse.net (631)582-4067

```html
<!DOCTYPE html>
<html lang="en">
<head>
<meta charset="utf-8">
<title>Copper Gavel Auctions – Business Card</title>
<link href="https://fonts.googleapis.com/css2?family=Michroma&family=Arimo:wght@400;700&display=swap" rel="stylesheet">
<style>
  :root {
    --backdrop: #bdbdbf;
    --navy: #0e3f80;
    --navy-deep: #1c3a78;
    --red: #d11a24;
    --white: #ffffff;
    --ink-blue: #1d3f86;
    --faint: #f1f1f3;
  }
  * { box-sizing: border-box; margin: 0; padding: 0; }
  html, body {
    width: 1200px; height: 900px; overflow: hidden;
    background: var(--backdrop);
  }
  .stage { position: relative; width: 1200px; height: 900px; }

  .card {
    position: absolute;
    width: 540px; height: 309px;
    border-radius: 26px;
    overflow: hidden;
    box-shadow: 0 6px 16px rgba(0,0,0,0.25);
  }

  /* Front */
  .card--front {
    left: 50px; top: 140px;
    background: linear-gradient(155deg, var(--navy) 0%, #4a2e64 45%, var(--red) 85%);
    display: flex; align-items: center; justify-content: center;
  }
  .brand {
    display: flex; align-items: center; gap: 16px;
  }
  .brand__dot {
    width: 46px; height: 46px; border-radius: 50%;
    flex-shrink: 0;
  }
  .brand__name {
    font-family: "Michroma", sans-serif;
    text-transform: uppercase;
    letter-spacing: 1px;
    line-height: 1.25;
  }
  .card--front .brand__dot { background: var(--white); }
  .card--front .brand__name { color: var(--white); font-size: 26px; }

  /* Back */
  .card--back {
    left: 610px; top: 450px;
    background: var(--white);
  }
  .card--back .decor {
    position: absolute; right: -60px; top: -40px;
    width: 300px; height: 300px; border-radius: 50%;
    background: var(--faint);
  }
  .card--back .brand {
    position: absolute; left: 34px; top: 48px;
  }
  .card--back .brand__dot { background: var(--red); width: 40px; height: 40px; }
  .card--back .brand__name { color: var(--red); font-size: 20px; }

  .person {
    position: absolute; left: 34px; top: 160px;
    font-family: "Michroma", sans-serif;
    font-size: 14px; letter-spacing: 3px;
    color: var(--red); text-transform: uppercase;
  }
  .contacts {
    position: absolute; left: 34px; top: 196px;
    list-style: none;
    font-family: "Arimo", sans-serif;
    font-size: 15px; color: var(--ink-blue);
  }
  .contacts li { display: flex; align-items: center; gap: 8px; margin-bottom: 6px; }
  .contacts svg { width: 14px; height: 14px; fill: none; stroke: var(--red); stroke-width: 2; }
  .contacts .accent { color: var(--red); }

  .address {
    position: absolute; right: 30px; top: 196px;
    font-family: "Arimo", sans-serif;
    font-size: 14px; line-height: 1.45;
    color: var(--ink-blue); text-align: right;
  }
</style>
</head>
<body>
<main class="stage">
  <section class="card card--front" aria-label="Card front">
    <div class="brand">
      <span class="brand__dot"></span>
      <span class="brand__name">Copper Gavel<br>Auctions</span>
    </div>
  </section>

  <section class="card card--back" aria-label="Card back">
    <div class="decor"></div>
    <div class="brand">
      <span class="brand__dot"></span>
      <span class="brand__name">Copper Gavel<br>Auctions</span>
    </div>

    <p class="person">Marcus Delvane</p>

    <ul class="contacts">
      <li>
        <svg viewBox="0 0 16 16"><path d="M3 1.5l3 3-1.5 2a9 9 0 0 0 5 5l2-1.5 3 3-2 2A13 13 0 0 1 1 3.5z"/></svg>
        (631)582-4067
      </li>
      <li>
        <svg viewBox="0 0 16 16"><rect x="1" y="3" width="14" height="10"/><path d="M1 3l7 6 7-6"/></svg>
        info@Copperbidhouse.net
      </li>
      <li>
        <svg viewBox="0 0 16 16"><circle cx="8" cy="8" r="6.5"/><path d="M1.5 8h13M8 1.5c-3 3.5-3 9.5 0 13M8 1.5c3 3.5 3 9.5 0 13"/></svg>
        www.<span class="accent">Copperbidhouse</span>.net
      </li>
    </ul>

    <p class="address">418 Birchmont Road Suite<br>200C Fenwick NY 11093</p>
  </section>
</main>
</body>
</html>
```